Overseas Property Tax Depreciation

We need a two sided flyer to promote our business and explain what we do. our website is www.tolvexhq.net.
The attached word file is what I would like on an A5 size flyer with one side showing the FAQ and the other the worked example. I would like these formatted much better than the are and in general style of the website. I will attach files for logos as well.

Business

```html
<!DOCTYPE html>
<html lang="en">
<head>
<meta charset="utf-8">
<title>Tolvex Tax Depreciation – FAQ</title>
<link rel="stylesheet" href="https://fonts.googleapis.com/css2?family=Didact+Gothic&family=Poppins:wght@500;600&display=swap">
<style>
:root{
  --green:#1b7b3a;
  --orange:#f39c1e;
  --yellow:#f2c230;
  --band:#5bab3f;
  --ink:#1d1d1d;
  --seal:#ececec;
  --seal-edge:#bdbdbd;
  --paper:#ffffff;
}
*{box-sizing:border-box;margin:0;padding:0}
html,body{width:846px;height:1200px;overflow:hidden;background:var(--paper)}
body{font-family:"Didact Gothic","Century Gothic",sans-serif;color:var(--ink)}
.flyer{position:relative;width:846px;height:1200px;overflow:hidden}

.member-name{position:absolute;left:38px;top:52px;font-family:"Didact Gothic",sans-serif;font-size:24px;color:var(--ink)}
.brand{position:absolute;left:0;right:0;top:40px;text-align:center;font-family:"Poppins",sans-serif;font-weight:600;color:var(--orange);line-height:1}
.brand-name{font-size:52px}
.brand-line{font-size:32px;margin-top:4px}
.registration{position:absolute;right:44px;top:42px;width:90px;text-align:center;font-family:Arial,sans-serif;font-size:9px;line-height:1.2;color:#333}
.seal{width:74px;height:74px;border-radius:50%;background:var(--seal);border:3px solid var(--seal-edge);margin:0 auto 12px}

.section{position:absolute;left:0;right:0}
.tab{display:flex;align-items:center;height:31px;background:var(--green);color:#fff;font-family:"Poppins",sans-serif;font-weight:600;font-size:18.5px;padding-left:34px;border-radius:0 12px 12px 0;line-height:1.2}
.tab.wide{height:61px;width:811px;font-size:19px;padding-right:20px}
.copy{padding:0 34px 0 34px;margin-top:19px}
.copy p,.copy li{font-size:13.6px;line-height:17px}
.copy p+p{margin-top:6px}
.points{list-style:none;margin-top:6px}
.points li{position:relative;padding-left:18px}
.points li+li{margin-top:6px}
.points li::before{content:"";position:absolute;left:2px;top:6px;width:5px;height:5px;background:var(--ink);transform:rotate(45deg)}
.points.tight{margin-top:6px}

.s1{top:169px}.s1 .tab{width:174px}
.s2{top:545px}.s2 .tab{width:573px}
.s3{top:678px}.s3 .tab{width:283px}
.s4{top:793px}.s4 .tab{width:354px}
.s5{top:1050px}

.footer-rule{position:absolute;left:0;right:0;bottom:26px;height:3px;background:var(--yellow)}
.footer-band{position:absolute;left:0;right:0;bottom:0;height:26px;background:var(--band)}
</style>
</head>
<body>
<main class="flyer">
  <header>
    <div class="member-name">Kestrel Guild</div>
    <div class="brand">
      <div class="brand-name">Tolvex</div>
      <div class="brand-line">tax depreciation</div>
    </div>
    <div class="registration">
      <div class="seal"></div>
      Tax agent<br>31847206
    </div>
  </header>

  <section class="section s1">
    <h2 class="tab">Why use us?</h2>
    <div class="copy">
      <p>There are several websites out there offering tax depreciation reports for Australian properties but there are very few who are appropriately qualified and approved by the Australian Tax Office (ATO) and offer the necessary Irish expertise. The Quantity Surveyor that prepares your report:</p>
      <ul class="points">
        <li>is Irish and qualified as a Quantity Surveyor in Ireland.</li>
        <li>worked there during the “Celtic Tiger” period when construction costs were quite high.</li>
        <li>has detailed knowledge of Irish construction methods and costs over the past 20 years. Irish buildings are generally much more expensive than Australia due to the climate, just think about how many Australian houses you have seen that have double glazing, central heating, insulation etc..</li>
        <li>has a partnership arrangement with an Irish quantity surveying firm to carry out the property inspections required in most cases to maximize the deductions available.</li>
        <li>is a chartered member of the Kestrel Guild.</li>
        <li>Maintains the Appropriate Professional Indemnity Insurance.</li>
        <li>Is registered with the Tax Practitioners Board. All quantity surveyors who prepare Property Tax Depreciation Schedules are required by the ATO to be registered with the Tax Practitioners Board which checks that the person preparing the reports is suitably qualified and maintains the appropriate professional indemnity insurance. You can check the registration on the TPB website. Our registration number is 31847206.</li>
      </ul>
    </div>
  </section>

  <section class="section s2">
    <h2 class="tab">My property is in Ireland does this make a difference?</h2>
    <div class="copy">
      <p>Division 43 of the Income Tax Assessment Act 1997 which deals with capital works depreciation states that it applies to buildings begun outside Australia after 21 August 1990 Sect 43.20 (1) (b). Your Australian tax return should cover your worldwide income. As long as the property is available to rent back in Ireland you are obliged by the ATO to report any income or loss on that property.</p>
    </div>
  </section>

  <section class="section s3">
    <h2 class="tab">Is my property too old?</h2>
    <div class="copy">
      <p>No, if your property was constructed after 1990 you can claim for both the construction cost element and the Plant and equipment. If it was built before then you can still claim the plant and equipment allowance. The easiest thing to do is to contact us with some details on your property and we can make an initial assessment of the possible annual savings.</p>
    </div>
  </section>

  <section class="section s4">
    <h2 class="tab">What is Property Depreciation?</h2>
    <div class="copy">
      <p>Just like you claim wear and tear on a car purchased for income producing purposes, you can also claim the depreciation of your investment property against your taxable income.</p>
      <p>There are 2 types available: depreciation on Plant and Equipment, and depreciation on the cost of construction. Plant and Equipment refers to items within the building like ovens, dishwashers, carpet and blinds etc. Both these costs can be offset against your assessable income.</p>
      <p>How much will the report cost?</p>
      <p>Each scenario is different so contact us to obtain a quick quote for your situation. Generally the cost of the report is a fraction of the savings in any one year.</p>
      <ul class="points tight">
        <li>Our fee is fully tax deductible</li>
        <li>You do NOT need to get this report done every year so the cost can be spread over several years</li>
      </ul>
    </div>
  </section>

  <section class="section s5">
    <h2 class="tab wide">I haven’t included my property for the past couple of years on my tax return is this a problem?</h2>
    <div class="copy">
      <p>No, in actual fact you could have been missing out on savings for a number of years, you can also use this report to claim a refund from the ATO for up to the past three years.</p>
    </div>
  </section>

  <div class="footer-rule"></div>
  <div class="footer-band" role="img" aria-label="Green dotted decorative band along the bottom edge"></div>
</main>
</body>
</html>
```